Harborline Tech & Security

need a new business card design for our Technology & Security Company. We are a Computer Networking Company, Security Camera Installers, Phone Systems.

Target Market(s)

Construction, Medical, Law Offices, Accounting, Retail etc.

Industry/Entity Type

Information Technology

Logo is attached, colors are Blue, Red, Black. Blue for Technology & Red is for Security Cameras, Access Control, Alarm Systems

Colors
fbed22
ec1f27
0555a3
ffffff

Requirements
Must have
• Pictures or Icons for
• For Technology:
• Computer, Network, Phone System, Copier, TV, Cabling
• For Security:
• Video Surveillance, Access Control, Intercom, Fire Alarm, Burglar Alarm, Time Clock

```html
<!DOCTYPE html>
<html lang="en">
<head>
<meta charset="utf-8">
<title>Harborline Tech &amp; Security – Business Card</title>
<link href="https://fonts.googleapis.com/css2?family=Open+Sans:wght@400;600;700;800&display=swap" rel="stylesheet">
<style>
  :root {
    --stage: #d9d9d9;
    --ink: #111111;
    --card-black: #050505;
    --paper: #ffffff;
    --paper-shade: #ececec;
    --tech-blue: #0b66ab;
    --security-red: #d01c22;
    --label-blue: #1f73c4;
    --label-red: #ec1f27;
    --white: #ffffff;
  }
  * { box-sizing: border-box; margin: 0; padding: 0; }
  html, body { width: 1200px; height: 904px; overflow: hidden; }
  body {
    background: var(--stage);
    font-family: "Open Sans", sans-serif;
    display: flex;
    flex-direction: column;
    align-items: center;
    justify-content: center;
    gap: 48px;
  }
  .card {
    position: relative;
    width: 640px;
    height: 366px;
    overflow: hidden;
    box-shadow: 0 10px 24px rgba(0,0,0,0.18);
  }

  /* brand name */
  .brand {
    display: flex;
    align-items: center;
    gap: 10px;
    justify-content: center;
  }
  .brand-dot {
    width: 14px; height: 14px; border-radius: 50%;
    background: var(--tech-blue);
  }
  .brand-name {
    font-weight: 800;
    font-size: 27px;
    letter-spacing: 0.5px;
    text-transform: uppercase;
  }

  /* back side */
  .card-back { background: var(--card-black); color: var(--white); }
  .card-back .brand { position: absolute; top: 98px; left: 0; right: 0; }
  .card-back .brand-name { color: var(--white); }
  .services {
    position: absolute; top: 190px; left: 0; right: 0;
    text-align: center;
    font-size: 14.5px;
    line-height: 1.55;
  }
  .services-label { font-weight: 700; }
  .services-label.tech { color: var(--label-blue); }
  .services-label.security { color: var(--label-red); }

  /* front side */
  .card-front {
    background: linear-gradient(180deg, var(--paper-shade) 0%, var(--paper) 55%);
  }
  .card-front .brand { position: absolute; top: 104px; left: 0; right: 0; }
  .card-front .brand-name { color: var(--ink); }
  .card-front .bands { position: absolute; inset: 0; }
  .holder {
    position: absolute; right: 270px; top: 266px;
    text-align: right; color: var(--white);
  }
  .holder-name { font-size: 22px; font-weight: 600; }
  .holder-role { font-size: 14px; opacity: 0.85; }
  .contact {
    position: absolute; left: 420px; top: 214px;
    color: var(--white);
    font-size: 14px;
    line-height: 1.5;
  }
  .contact-address { margin-bottom: 6px; }
  .contact-row { display: flex; align-items: center; gap: 8px; }
  .contact-row svg { width: 13px; height: 13px; flex: none; }
</style>
</head>
<body>

  <section class="card card-back">
    <div class="brand">
      <span class="brand-dot"></span>
      <span class="brand-name">Harborline Tech</span>
    </div>
    <div class="services">
      <div class="services-label tech">Technology:</div>
      <div>Computer, Network, Phone System, Copier, TV, Cabling</div>
      <div class="services-label security">Security:</div>
      <div>Video Surveillance, Access Control, Intercom, Fire Alarm, Burglar Alarm, Time Clock</div>
    </div>
  </section>

  <section class="card card-front">
    <svg class="bands" viewBox="0 0 640 366" width="640" height="366" aria-hidden="true">
      <polygon points="380,196 640,196 640,366 430,366" fill="var(--security-red)"/>
      <polygon points="0,236 392,236 430,366 0,366" fill="var(--tech-blue)"/>
    </svg>
    <div class="brand">
      <span class="brand-dot"></span>
      <span class="brand-name">Harborline Tech</span>
    </div>
    <div class="holder">
      <div class="holder-name">Ethan Carver</div>
      <div class="holder-role">Manager</div>
    </div>
    <div class="contact">
      <div class="contact-address">48 Harbor Lane, Suite 12<br>Eastfield, CA 95012.</div>
      <div class="contact-row">
        <svg viewBox="0 0 16 16"><path d="M3 1.5l3 .5 1 3.5-2 1.2a9 9 0 0 0 4.3 4.3l1.2-2 3.5 1 .5 3c-.3 1-1.2 1.5-2.2 1.5C6.5 14.5 1.5 9.5 1.5 3.7 1.5 2.7 2 1.8 3 1.5z" fill="#fff"/></svg>
        <span>+1 555 0142 3380</span>
      </div>
      <div class="contact-row">
        <svg viewBox="0 0 16 16"><rect x="1" y="3" width="14" height="10" rx="1" fill="#fff"/><path d="M1.5 3.5L8 9l6.5-5.5" fill="none" stroke="var(--security-red)" stroke-width="1.4"/></svg>
        <span>info@harborlinetech.com</span>
      </div>
      <div class="contact-row">
        <svg viewBox="0 0 16 16"><circle cx="8" cy="8" r="6.5" fill="none" stroke="#fff" stroke-width="1.4"/><ellipse cx="8" cy="8" rx="2.8" ry="6.5" fill="none" stroke="#fff" stroke-width="1.2"/><path d="M1.5 8h13" stroke="#fff" stroke-width="1.2"/></svg>
        <span>www.harborlinetech.com</span>
      </div>
    </div>
  </section>

</body>
</html>
```